Web Design for "Global Broadcasting Service Business"

We are a satellite company launching a new exciting brand by the name of "Pelumo". Pelumo is a broadcasting solution provider that gives end-to-end solutions to TV channels and other content providers to deliver and distribute their content globally. Weather it be TV channels that need to be broadcasted in their local regions or internationally, or its collection of news from various locations, or even coverage of special sports or other events, we provide the technology and services to make that happen. This allows the broadcaster to focus on the content rather than worry about the logistics of how it will get to its viewers. We can help place their content to regional cable and satellite operators. Moreover we can provide services for content creation and coverage of major sports, news and special events. Pelumo is one-stop-shop for all broadcast solutions

We want a 20 page static website. I am mentioning certain key competitors of ours so that you can have a look at the comparable look we are anticipating in the design

www.orvenmedia.tv
www.dunharlow.com
www.pembrick.com

Its a global company so the design has to give the same look and feel

Target Market(s)

TV Channel Owners and their Technical Heads

Industry/Entity Type

Business

Requirements
Must have
• We want the designers to submit the home page design first giving us the look and feel of the website design. you can use sample text and any satellite based image to start off. Once we shortlist the best home page designs we will ask you to create the remaining pages.

The most work is on the home page, remaining subsections will only require a change in text and images at most. the overall look and feel of the website including headers and footers will remain the same

```html
<!DOCTYPE html>
<html lang="en">
<head>
<meta charset="utf-8">
<title>Pelumo – Regional Solution, Global Distribution</title>
<link rel="stylesheet" href="https://fonts.googleapis.com/css2?family=Questrial&family=Poppins:wght@500;600;700&display=swap">
<style>
  :root {
    --brand-red: #c8264a;
    --brand-red-dark: #9c1030;
    --brand-red-light: #e06a85;
    --ink: #1b1b1b;
    --ink-soft: #6d6d6d;
    --rule: #d8d8d8;
    --page: #f6f6f6;
    --footer-dark: #2a2a2a;
    --white: #ffffff;
  }
  * { box-sizing: border-box; margin: 0; padding: 0; }
  html, body { width: 1200px; height: 900px; overflow: hidden; }
  body {
    position: relative;
    background: var(--page);
    font-family: "Questrial", "Century Gothic", sans-serif;
    color: var(--ink);
  }
  a { color: inherit; text-decoration: none; }

  .top-bar {
    position: absolute; left: 100px; top: 0; width: 1000px; height: 12px;
    background: linear-gradient(90deg, var(--brand-red-dark), var(--brand-red) 50%, var(--brand-red-dark));
  }

  /* Header */
  .site-header { position: absolute; left: 0; top: 12px; width: 1200px; height: 134px; background: var(--white); }
  .brand { position: absolute; left: 100px; top: 44px; display: flex; flex-direction: column; }
  .brand-row { display: flex; align-items: center; gap: 8px; }
  .brand-mark { width: 14px; height: 14px; background: var(--brand-red); }
  .brand-name { font-size: 50px; line-height: 50px; color: var(--ink); letter-spacing: -1px; }
  .brand-tagline { font-size: 10px; margin-top: 6px; color: var(--ink); font-family: "Poppins", sans-serif; font-weight: 500; }

  .utility-links { position: absolute; right: 100px; top: 14px; display: flex; gap: 18px; font-size: 13px; }
  .utility-links .active { color: var(--brand-red); }

  .social-links { position: absolute; left: 570px; top: 45px; display: flex; gap: 6px; }
  .social-links span { width: 21px; height: 21px; background: #4a4a4a; border-radius: 3px; display: block; }

  .search { position: absolute; left: 669px; top: 43px; display: flex; gap: 6px; }
  .search-input {
    width: 299px; height: 26px; border: 1px solid #d0d0d0; background: #ececec;
    font: 14px "Questrial", sans-serif; color: #9a9a9a; padding: 0 9px; line-height: 24px;
  }
  .search-button {
    width: 126px; height: 26px; background: var(--brand-red); color: var(--white);
    border: 1px dashed #f0a0b0; font: 600 15px "Poppins", sans-serif;
    display: flex; align-items: center; justify-content: center; gap: 4px;
  }

  .main-nav { position: absolute; left: 363px; top: 92px; display: flex; font-size: 14px; }
  .main-nav a { position: relative; padding-bottom: 16px; }
  .main-nav a.current { color: var(--brand-red); border-bottom: 2px solid var(--brand-red); }
  .main-nav .sep { color: #999; margin: 0 15px; }
  .header-rule { position: absolute; left: 100px; top: 131px; width: 1000px; height: 1px; background: var(--rule); }

  /* Hero */
  .hero {
    position: absolute; left: 0; top: 146px; width: 1200px; height: 292px;
    background: radial-gradient(ellipse at 75% 20%, #7fa6c8 0%, #355f8a 28%, #12263f 55%, #050b16 100%);
  }
  .hero-caption {
    position: absolute; left: 633px; top: 135px; width: 467px; height: 120px;
    background: rgba(20, 20, 20, 0.72); color: var(--white);
  }
  .hero-caption .line-1 { position: absolute; left: 15px; top: 4px; font: 700 60px/70px "Poppins", sans-serif; }
  .hero-caption .line-1 small { font: 600 34px "Poppins", sans-serif; color: #cfcfcf; margin-left: 6px; }
  .hero-caption .line-2 { position: absolute; right: 12px; top: 72px; font: 600 29px/40px "Poppins", sans-serif; }
  .hero-dots { position: absolute; left: 546px; top: 231px; display: flex; gap: 5px; }
  .hero-dots span { width: 12px; height: 12px; border-radius: 50%; background: #333; }
  .hero-dots span:last-child { background: #666; }

  /* Service strip */
  .services {
    position: absolute; left: 100px; top: 401px; width: 1000px; height: 157px; background: var(--brand-red);
  }
  .services-edge {
    position: absolute; left: 100px; top: 558px; width: 1000px; height: 8px;
    background: linear-gradient(var(--brand-red-light), #c88a98);
  }
  .service { position: absolute; top: 20px; width: 204px; text-align: center; color: var(--white); }
  .service-photo { width: 204px; height: 78px; border: 1px solid rgba(255,255,255,0.5); box-shadow: 0 6px 8px rgba(0,0,0,0.3); }
  .service-title { margin-top: 19px; font-size: 19px; }
  .services-pointer { position: absolute; left: 145px; top: 149px; }

  /* Welcome */
  .welcome { position: absolute; left: 100px; top: 598px; width: 727px; }
  .welcome h1 { font: 600 22px "Poppins", sans-serif; letter-spacing: 0.3px; padding-bottom: 4px; border-bottom: 1px solid var(--rule); }
  .welcome h1 em { font-style: normal; color: var(--brand-red); }
  .welcome p { margin-top: 12px; font-size: 13.5px; line-height: 22px; color: var(--ink-soft); }
  .read-more { position: absolute; right: 0; top: 134px; font: 500 13px "Poppins", sans-serif; color: var(--ink); }
  .welcome-photo {
    position: absolute; left: 843px; top: 603px; width: 257px; height: 143px;
    background: linear-gradient(180deg, #b9cfe4 0%, #8a9aa8 45%, #5d6a5a 78%, #7a9a58 100%);
    border: 1px solid #ccc;
  }

  /* Footer */
  .site-footer { position: absolute; left: 100px; top: 770px; width: 1000px; height: 120px; display: flex; }
  .footer-links { width: 742px; background: var(--brand-red); position: relative; color: var(--white); }
  .footer-col { position: absolute; top: 12px; width: 128px; }
  .footer-col h2 { font-size: 14px; font-weight: 400; padding-bottom: 5px; border-bottom: 1px solid rgba(255,255,255,0.35); margin-bottom: 17px; }
  .footer-col li { list-style: none; font-size: 13px; line-height: 20px; }
  .footer-contact { width: 258px; background: var(--footer-dark); color: var(--white); padding: 12px 0 0 13px; }
  .footer-contact h2 { width: 215px; font-size: 14px; font-weight: 400; padding-bottom: 5px; border-bottom: 1px solid #666; margin-bottom: 17px; }
  .contact-links { font-size: 14px; }
  .contact-links .sep { color: #888; margin: 0 20px; }
  .legal { margin-top: 9px; font: 12px/21px Arial, sans-serif; }
  .legal a { color: var(--brand-red); }
  .bottom-band { position: absolute; left: 100px; top: 890px; width: 1000px; height: 10px; background: #303030; }
</style>
</head>
<body>
  <div class="top-bar"></div>

  <header class="site-header">
    <a class="brand" href="#">
      <span class="brand-row"><span class="brand-name">Pelumo</span><span class="brand-mark"></span></span>
      <span class="brand-tagline">Regional Solution, Global Distribution</span>
    </a>

    <nav class="utility-links">
      <a class="active" href="#">Careers</a>
      <a href="#">Contact Us</a>
      <a href="#">Blog</a>
    </nav>

    <div class="social-links" aria-label="Social links"><span></span><span></span><span></span></div>

    <form class="search">
      <div class="search-input">type your text here . . .</div>
      <div class="search-button">Search
        <svg width="13" height="13" viewBox="0 0 13 13" aria-hidden="true"><circle cx="5.5" cy="5.5" r="4" fill="none" stroke="#fff" stroke-width="2"/><line x1="8.5" y1="8.5" x2="12" y2="12" stroke="#fff" stroke-width="2"/></svg>
      </div>
    </form>

    <nav class="main-nav">
      <a class="current" href="#">Homepage</a><span class="sep">|</span>
      <a href="#">Who we are</a><span class="sep">|</span>
      <a href="#">Broadcast Solutions</a><span class="sep">|</span>
      <a href="#">On-Demand Services</a><span class="sep">|</span>
      <a href="#">Global Network</a><span class="sep">|</span>
      <a href="#">Beams</a>
    </nav>
    <div class="header-rule"></div>
  </header>

  <section class="hero" role="img" aria-label="Satellite orbiting above the blue Earth in space">
    <div class="hero-dots"><span></span><span></span><span></span><span></span></div>
    <div class="hero-caption">
      <div class="line-1">HIGH<small>Throughput</small></div>
      <div class="line-2">Satellite Technology</div>
    </div>
  </section>

  <section class="services">
    <div class="service" style="left:34px">
      <div class="service-photo" role="img" aria-label="Satellite dishes silhouetted at sunset" style="background:linear-gradient(180deg,#3c4a66 0%,#d9743a 55%,#2a1a14 100%)"></div>
      <div class="service-title">Teleport Facilities</div>
    </div>
    <div class="service" style="left:277px">
      <div class="service-photo" role="img" aria-label="Field of white satellite dishes below mountains" style="background:linear-gradient(180deg,#8fb0d4 0%,#b8c2c8 40%,#e8ebe8 65%,#5c8a3c 100%)"></div>
      <div class="service-title">Turnaround</div>
    </div>
    <div class="service" style="left:521px">
      <div class="service-photo" role="img" aria-label="Racks of broadcast equipment" style="background:linear-gradient(90deg,#3a3a3a,#6a6a6a 50%,#2e2e2e)"></div>
      <div class="service-title">MCPC Platforms</div>
    </div>
    <div class="service" style="left:764px">
      <div class="service-photo" role="img" aria-label="Playout control room with operators and monitors" style="background:linear-gradient(180deg,#2e3a30 0%,#5d7a5a 45%,#c9cfcf 100%)"></div>
      <div class="service-title">HD/3D Playout Center</div>
    </div>
    <svg class="services-pointer" width="24" height="9" viewBox="0 0 24 9" aria-hidden="true"><polygon points="0,9 12,0 24,9" fill="#e06a85"/></svg>
  </section>
  <div class="services-edge"></div>

  <section class="welcome">
    <h1>WELCOME TO <em>OUR SITE</em></h1>
    <p>TV Distribution - Orvenlink delivers your content to every corner of the world.<br>
    Our Global Satellite and fiber network enables us to provide high end TV Distribution services, allowing our clients to distribute their content easily to direct to home viewers (DTH), contribution to Cable operators and IPTV platforms in every corner of the world</p>
    <a class="read-more" href="#">READ MORE</a>
  </section>
  <div class="welcome-photo" role="img" aria-label="Modern glass office building with lawn"></div>

  <footer class="site-footer">
    <div class="footer-links">
      <div class="footer-col" style="left:22px">
        <h2>Who we are ?</h2>
        <ul><li>Philosophy</li><li>Fast facts</li><li>Executive team</li></ul>
      </div>
      <div class="footer-col" style="left:200px">
        <h2>What &nbsp;We Do ?</h2>
        <ul><li>Deliver content</li><li>Distribute content</li><li>Cover major events</li></ul>
      </div>
      <div class="footer-col" style="left:387px">
        <h2>Where We Are</h2>
        <ul><li>Offices</li></ul>
      </div>
      <div class="footer-col" style="left:569px">
        <h2>What's New</h2>
        <ul><li>News</li><li>Download zone</li></ul>
      </div>
    </div>
    <div class="footer-contact">
      <h2>Contact us</h2>
      <div class="contact-links"><a href="#">Directory</a><span class="sep">|</span><a href="#">Contact form</a></div>
      <div class="legal">Copyright © 2014 &nbsp;<a href="#">pelumo.com</a><br>All Rights Reserved | <a href="#">Privacy Policy</a></div>
    </div>
  </footer>
  <div class="bottom-band"></div>
</body>
</html>
```